Healthcare Service Provider looking for PowerPoint Template

ROV Profile of the company & business activity
===================================
ROV is the leading after-sale healthcare services provider in Kuwait. The IT department in the company sells & executes Healthcare IT projects in hospitals that mainly cover:

1. IT Infrastructure covering data center, disaster recovery, servers, virtualization, backup, redundancy & high-availability, multi-site connectivity, wired & wireless networking, OS & network management, software subscriptions, …etc.

2. Healthcare IT systems covering the Hospital Management system, Electronic Medical Record, evidence-based clinical content, clinical decision support systems, Radiology information system, Lab information system, pharmacy management system, ICU system, dental system, dietary & nutrition system, integration with 3rd party systems in the hospital

3. Human resources covering the company specialized teams of clinical informatics specialists, pharmacists, nurses, project managers, user experience specialists, integration specialists, systems analysts, systems developers, DB administrators, Network administrators, system architects, systems engineers, …

The assortment of these professionals handle the services for implementing specialty Healthcare IT systems, training hospital staff & healthcare professionals, on-site support & maintenance of implemented healthcare systems at the hospital

Requested design job
================
We require a PowerPoint template to be used by the IT department in presenting sales & marketing pitches, commercial proposals, projects, and related to the business activities described in the profile.

The design of the PowerPoint template should:

. be personalized for the business activities of the IT department. promote the corporate brand identity of the company. provide clean, modern and fluent look & feel for presenting on screen, projector or printing. include font selection & design as part of the template design. light colored background

. multiple page layouts & slide types like a cover slide, title slide, different types of content slides, ….

. include design collaterals like icons and clip-arts

. have common design elements in PowerPoint Master slides

Included are the current corporate logos of the company.

In summary, simplicity, fluency and personality are key to the design we seek.

Requirements
Must have
• The design of the PowerPoint template should:
• . be personalized for the business activities of the IT department. promote the corporate brand identity of the company. provide clean, modern and fluent look & feel for presenting on screen, projector or printing. include font selection & design as part of the template design. light colored background
• . multiple page layouts & slide types like a cover slide, title slide, different types of content slides, ….
• . include design collaterals like icons and clip-arts
• . have common design elements in PowerPoint Master slides

```html
<!DOCTYPE html>
<html lang="en">
<head>
<meta charset="utf-8">
<title>ROV Healthcare IT – Presentation Template</title>
<link rel="stylesheet" href="https://fonts.googleapis.com/css2?family=Montserrat:wght@300;400;500;600;700&family=Tajawal:wght@500;700&display=swap">
<style>
  :root{
    --navy:#0d2640;
    --navy-deep:#0a2037;
    --ink:#1b2c44;
    --grey-text:#3c4450;
    --teal:#1a9a96;
    --sky:#7cc4ec;
    --sky-pale:#d6ecf8;
    --stage:#ececec;
    --white:#ffffff;
  }
  *{box-sizing:border-box;margin:0;padding:0}
  html,body{width:1200px;height:1200px;overflow:hidden}
  body{
    background:radial-gradient(circle at 60% 40%, #ffffff 0%, #f1f1f1 55%, var(--stage) 100%);
    font-family:"Montserrat",Arial,sans-serif;
    position:relative;
  }
  .slide{position:absolute;width:593px;height:444px;overflow:hidden;box-shadow:0 6px 16px rgba(0,0,0,.22)}

  /* ---------- cover slide ---------- */
  .slide--cover{left:70px;top:72px;background:linear-gradient(135deg,#e3e3e3 0%,#f7f7f7 40%,#ffffff 70%,#f4f4f4 100%)}
  .cover-pattern{position:absolute;inset:0;background:
      radial-gradient(circle at 20% 15%,rgba(200,200,200,.55),transparent 40%),
      radial-gradient(circle at 10% 75%,rgba(195,195,195,.5),transparent 45%)}
  .brand{position:absolute;text-align:center;color:var(--navy)}
  .brand__mark{display:flex;align-items:center;justify-content:center;gap:10px;font-weight:700;font-size:50px;letter-spacing:2px;line-height:1}
  .brand__mark::before{content:"";width:14px;height:14px;background:currentColor;border-radius:50%}
  .brand__name{font-size:13px;font-weight:400;margin-top:22px}
  .brand__name small{font-size:6px}
  .brand__arabic{font-family:"Tajawal",sans-serif;font-weight:700;font-size:15px;margin-top:2px}
  .brand__arabic small{font-size:7px;font-weight:500}
  .slide--cover .brand{left:0;right:0;top:48px}
  .cover-headline{position:absolute;left:0;right:0;top:186px;text-align:center;color:var(--navy);text-transform:uppercase}
  .cover-headline span.line{display:inline-block;border-bottom:1px solid var(--navy);padding:0 2px 2px}
  .cover-headline .l1{font-size:15px}
  .cover-headline .l2{font-size:15px;margin-top:6px}
  .cover-headline b{font-weight:700;font-size:19px}
  .cover-headline .big{font-size:22px;font-weight:400}
  .skyline{position:absolute;left:30px;bottom:0;width:380px;height:160px;
    background:linear-gradient(to top,rgba(60,70,90,.22),rgba(60,70,90,.04))}

  /* ---------- content slide ---------- */
  .slide--content{left:392px;top:359px;height:441px;background:var(--white)}
  .content-header{position:absolute;left:0;top:0;width:100%;height:164px;background:var(--navy)}
  .content-header h1{position:absolute;left:26px;top:50px;color:var(--white);font-weight:500;font-size:20px;letter-spacing:.5px}
  .content-header p{position:absolute;left:26px;top:89px;width:380px;color:var(--white);font-size:8.6px;line-height:1.42}
  .header-art{position:absolute;right:0;top:0}
  .rule-stack{position:absolute;left:0;top:165px;width:460px}
  .rule-stack i{display:block;height:1px;background:var(--navy);margin-bottom:4px}
  .service{position:absolute;left:60px;width:520px;height:64px}
  .service__icon{position:absolute;left:0;top:0;width:90px;text-align:center;color:var(--navy)}
  .service__icon svg{display:block;margin:0 auto 2px}
  .service__label{font-size:9.5px;line-height:1}
  .service__sub{font-size:4.6px;letter-spacing:.5px;display:block;margin-top:1px}
  .service__divider{position:absolute;left:95px;top:0;width:1px;height:58px;background:var(--navy)}
  .service__text{position:absolute;left:114px;top:12px;width:380px;font-size:8.6px;line-height:1.42;color:var(--grey-text)}

  /* ---------- closing slide ---------- */
  .slide--closing{left:562px;top:723px;width:592px;height:445px;background:var(--navy-deep)}
  .closing-art{position:absolute;left:0;top:0}
  .slide--closing .brand{left:30px;top:78px;color:var(--white);text-align:left}
  .slide--closing .brand__mark{justify-content:flex-start;margin-left:44px}
  .slide--closing .brand__name{margin-top:28px}
  .thank-you{position:absolute;left:160px;top:298px;width:280px;text-align:center;color:var(--white);font-size:20px;font-weight:300;letter-spacing:13px}
  .thank-you::after{content:"";display:block;height:1px;margin-top:6px;background:linear-gradient(90deg,transparent,#9fb3c7 20%,#9fb3c7 80%,transparent)}
</style>
</head>
<body>

<!-- Cover slide -->
<section class="slide slide--cover">
  <div class="cover-pattern"></div>
  <div class="brand">
    <div class="brand__mark">ROV</div>
    <div class="brand__name">Rovena Vital Systems <small>K.S.C.P.</small></div>
    <div class="brand__arabic" dir="rtl">شركة روفينا للأنظمة <small>ش.م.ك.ع.</small></div>
  </div>
  <div class="cover-headline">
    <span class="line l1"><b>ROV</b> is the <span class="big">Leading</span> after-sale <b>Healthcare</b></span><br>
    <span class="line l2">Services provider in <span class="big">Kuwait</span></span>
  </div>
  <div class="skyline" role="img" aria-label="Line drawing of the Kuwait City skyline with its towers"></div>
</section>

<!-- Content slide -->
<section class="slide slide--content">
  <div class="content-header">
    <h1>PRESENTATION TITLE</h1>
    <p>ROV is the leading after-sale healthcare services provider in Kuwait. The IT department in the company sells &amp; executes Healthcare IT projects in hospitals that mainly cover:</p>
    <svg class="header-art" width="160" height="164" viewBox="0 0 160 164" role="img" aria-label="Doctor's hand touching floating medical icons, seen through diagonal stripes">
      <defs>
        <linearGradient id="stripeFill" x1="0" y1="0" x2="1" y2="1">
          <stop offset="0" stop-color="#5fb3e6"/>
          <stop offset=".55" stop-color="#cfe7f5"/>
          <stop offset="1" stop-color="#f3f6f8"/>
        </linearGradient>
      </defs>
      <g fill="url(#stripeFill)" stroke-linecap="round">
        <path d="M40 36 L75 0 L110 0 L22 120 Q10 130 8 116 Q6 106 14 98 Z"/>
        <path d="M120 0 L155 0 L60 118 Q48 128 40 118 Q36 108 44 100 Z"/>
        <path d="M160 30 L160 70 L90 150 Q80 160 72 150 Q66 140 76 130 Z"/>
      </g>
    </svg>
  </div>
  <div class="rule-stack"><i></i><i></i><i style="width:96%"></i><i style="width:88%"></i></div>

  <div class="service" style="top:273px;top:272px;top:270px;top:196px">
    <div class="service__icon">
      <svg width="40" height="42" viewBox="0 0 40 42" fill="none" stroke="var(--teal)" stroke-width="2">
        <path d="M8 12 A16 16 0 0 1 30 6"/><path d="M32 30 A16 16 0 0 1 10 36"/>
        <path d="M28 2 L31 6 L26 8" /><path d="M12 40 L9 36 L14 34"/>
        <ellipse cx="20" cy="14" rx="8" ry="3"/><path d="M12 14 V28 Q20 32 28 28 V14"/><path d="M12 19 Q20 23 28 19"/><path d="M12 24 Q20 28 28 24"/>
      </svg>
      <div class="service__label">COVERING<span class="service__sub">DATA</span></div>
    </div>
    <div class="service__divider"></div>
    <div class="service__text">IT Infrastructure covering data center, disaster recovery, servers, virtualization, backup, redundancy &amp; high-availability, multi-site connectivity, wired &amp; wireless networking, OS &amp; network management, software subscriptions, ...etc.</div>
  </div>

  <div class="service" style="top:271px">
    <div class="service__icon">
      <svg width="54" height="30" viewBox="0 0 54 30" fill="none" stroke="var(--navy)" stroke-width="1.6">
        <rect x="18" y="2" width="18" height="26"/><rect x="4" y="12" width="14" height="16"/><rect x="36" y="12" width="14" height="16"/>
        <path d="M1 28 H53"/><rect x="24" y="21" width="6" height="7"/>
        <path d="M21 6 H33 M21 10 H33 M21 14 H33 M7 17 H15 M7 22 H15 M39 17 H47 M39 22 H47" stroke-dasharray="2 1.5"/>
      </svg>
      <div class="service__label">HOSPITAL<span class="service__sub">MANAGEMENT</span></div>
    </div>
    <div class="service__divider"></div>
    <div class="service__text">IT Infrastructure covering data center, disaster recovery, servers, virtualization, backup, redundancy &amp; high-availability, multi-site connectivity, wired &amp; wireless networking, OS &amp; network management, software subscriptions, ...etc.</div>
  </div>

  <div class="service" style="top:356px">
    <div class="service__icon">
      <svg width="34" height="34" viewBox="0 0 34 34" fill="none" stroke="#555" stroke-width="2.4">
        <path d="M6 10 A14 14 0 0 1 28 8"/><path d="M28 24 A14 14 0 0 1 6 26"/>
        <circle cx="17" cy="13" r="4.5" fill="#555"/><path d="M9 25 Q17 14 25 25 Z" fill="#555"/>
      </svg>
      <div class="service__label">HUMAN<span class="service__sub">RESOURCES</span></div>
    </div>
    <div class="service__divider"></div>
    <div class="service__text">IT Infrastructure covering data center, disaster recovery, servers, virtualization, backup, redundancy &amp; high-availability, multi-site connectivity, wired &amp; wireless networking, OS &amp; network management, software subscriptions, ...etc.</div>
  </div>
</section>

<!-- Closing slide -->
<section class="slide slide--closing">
  <svg class="closing-art" width="592" height="445" viewBox="0 0 592 445" role="img" aria-label="Doctor's hand touching a honeycomb of glowing medical care icons">
    <defs>
      <linearGradient id="closingFill" x1="0" y1="0" x2="1" y2="1">
        <stop offset="0" stop-color="#6cbcea"/>
        <stop offset=".45" stop-color="#bfe0f3"/>
        <stop offset=".75" stop-color="#eef3f6"/>
        <stop offset="1" stop-color="#d9e6ee"/>
      </linearGradient>
    </defs>
    <path d="M158 0 H592 V221 L516 297 Q490 320 466 300 Z" fill="url(#closingFill)"/>
  </svg>
  <div class="brand">
    <div class="brand__mark">ROV</div>
    <div class="brand__name">Rovena Vital Systems <small>K.S.C.P.</small></div>
    <div class="brand__arabic" dir="rtl">شركة روفينا للأنظمة <small>ش.م.ك.ع.</small></div>
  </div>
  <div class="thank-you">THANK YOU</div>
</section>

</body>
</html>
```